Poster Design for kebab shop products

need a new poster for our new blazer tray special, sign will be inside of shopping centre at different location to shop will need to stand out and draw customers to the store, MUST contain shops logo & picture added, poster size will be 76cm x 101cm so will need to suit that size

MUST ALSO CONTAIN THE FOLLOWING
Blazer Tray / HSP
Lamb & Chips
Chicken & Chips
Beef & Chips
+ Can $15

Target Market(s)

new customers

Industry/Entity Type

Retail

Font styles to use
Sans Serif

Colors

Designer to choose colors to be used in the design.

Requirements
Must have
• company logo
• picture of blazr tray provided
• Blazer Tray / HSP
• Lamb & Chips
• Chicken & Chips
• Beef & Chips
• + Can $15

```html
<!DOCTYPE html>
<html lang="en">
<head>
<meta charset="utf-8">
<title>Blazer Tray Special Poster</title>
<link rel="stylesheet" href="https://fonts.googleapis.com/css2?family=Chewy&family=Permanent+Marker&display=swap">
<style>
  :root {
    --page-bg: #f2f2f2;
    --sky-deep: #1f4fbf;
    --sky-mid: #4f86dc;
    --sea: #3b9ab8;
    --sea-light: #8fc9d6;
    --sand: #e99a45;
    --sand-light: #f6c98c;
    --glow: #fffaf0;
    --price-red: #d51f35;
    --text-white: #ffffff;
    --text-orange: #f5981c;
    --text-shadow: #1a1a2a;
    --foam: #f4f4f2;
    --brand-red: #d2202f;
  }
  * { box-sizing: border-box; margin: 0; padding: 0; }
  html, body {
    width: 1200px;
    height: 1200px;
    overflow: hidden;
    background: var(--page-bg);
  }
  .poster {
    position: absolute;
    left: 190px;
    top: 45px;
    width: 820px;
    height: 1110px;
    overflow: hidden;
  }
  .poster__scenery {
    position: absolute;
    inset: 0;
    background:
      radial-gradient(ellipse 55% 22% at 50% 86%, var(--glow) 0%, rgba(255,250,240,0.6) 45%, rgba(255,250,240,0) 100%),
      radial-gradient(circle at 84% 11%, rgba(255,255,255,0.95) 0%, rgba(255,255,255,0.3) 6%, rgba(255,255,255,0) 14%),
      linear-gradient(to bottom,
        var(--sky-deep) 0%,
        var(--sky-mid) 38%,
        var(--sea) 48%,
        var(--sea-light) 62%,
        var(--sand-light) 70%,
        var(--sand) 100%);
  }
  .poster__tray {
    position: absolute;
    left: 95px;
    top: 15px;
    width: 565px;
    height: 505px;
    border-radius: 60px 60px 40px 40px;
    background:
      radial-gradient(ellipse 45% 28% at 50% 48%, #b0432e 0%, #8a4a2a 55%, rgba(138,74,42,0) 100%),
      radial-gradient(ellipse 48% 36% at 50% 55%, #e9d56a 0%, #d9b44c 60%, rgba(217,180,76,0) 100%),
      var(--foam);
    box-shadow: 0 10px 30px rgba(0,0,0,0.25);
  }
  .poster__price {
    position: absolute;
    left: 262px;
    top: -8px;
    width: 240px;
    height: 240px;
    border-radius: 50%;
    background: var(--price-red);
    display: flex;
    align-items: center;
    justify-content: center;
    padding-top: 30px;
    font-family: "Permanent Marker", cursive;
    font-size: 108px;
    color: var(--text-white);
    transform: rotate(-6deg);
  }
  .poster__menu {
    position: absolute;
    left: 0;
    right: 0;
    top: 578px;
    text-align: center;
    font-family: "Chewy", sans-serif;
    font-size: 68px;
    line-height: 60px;
    color: var(--text-white);
    text-shadow: 3px 3px 0 var(--text-shadow), 0 0 6px rgba(0,0,0,0.5);
    letter-spacing: 1px;
  }
  .poster__menu-line { display: block; }
  .poster__menu-line--blazer { padding-left: 30px; }
  .poster__menu-line--lamb { padding-left: 30px; }
  .poster__menu-line--chicken { padding-left: 50px; }
  .poster__menu-line--beef { padding-left: 30px; }
  .accent { color: var(--text-orange); }
  .brand {
    position: absolute;
    left: 0;
    right: 0;
    top: 900px;
    display: flex;
    align-items: center;
    justify-content: center;
    gap: 18px;
  }
  .brand__dot {
    width: 64px;
    height: 64px;
    border-radius: 50%;
    background: var(--text-orange);
  }
  .brand__name {
    font-family: "Chewy", sans-serif;
    font-size: 64px;
    color: var(--brand-red);
  }
</style>
</head>
<body>
  <main class="poster">
    <div class="poster__scenery" role="img" aria-label="Beach scene: blue sky with sun, ocean and golden sand"></div>
    <div class="poster__tray" role="img" aria-label="Photo: Blazer Tray of kebab meat and chips with garlic and chilli sauce in a foam container"></div>
    <div class="poster__price">$15</div>
    <p class="poster__menu">
      <span class="poster__menu-line poster__menu-line--blazer">blazer tray / HSP</span>
      <span class="poster__menu-line poster__menu-line--lamb accent">Lamb &amp; Chips</span>
      <span class="poster__menu-line poster__menu-line--chicken">Chicken &amp; Chips</span>
      <span class="poster__menu-line poster__menu-line--beef"><span class="accent">Beef &amp; Chips</span> + can</span>
    </p>
    <div class="brand">
      <span class="brand__dot"></span>
      <span class="brand__name">Skewer Cove</span>
    </div>
  </main>
</body>
</html>
```